Post card for landscape service

Velmora Property Management**FEATURED SERVICE*** Weekly Lawn mowing service starting at $15/ cutting ****other services****landscape servicespring and fall clean uplawn and flowerbed care (pest and weed control)fertilizing plantingand moreCall for a Free estimate!!10% off first months service with signed contract

Please make double sided ( a front and a back)

Target Market(s)

home owners

Industry/Entity Type

Landscape

Requirements
Must have
• please feture the weekly lawn mowing service and then list the other sevices
• contact info... can be found on business card that was uploaded.
• must say residential services
Should not have
• please dont list reo management

```html
<!DOCTYPE html>
<html lang="en">
<head>
<meta charset="utf-8">
<title>Velmora Property Management – Postcard</title>
<link rel="stylesheet" href="https://fonts.googleapis.com/css2?family=Oswald:wght@500;600;700&family=Archivo+Black&family=Open+Sans:wght@600;800&display=swap">
<style>
  :root {
    --page: #f2f4f0;
    --green-deep: #0d6b0d;
    --green: #1a8a14;
    --green-bright: #3fae1c;
    --green-pale: #eef6dc;
    --green-soft: #c9e39a;
    --silver: #d7dad6;
    --ink: #141414;
    --slate: #3a4048;
    --white: #ffffff;
  }
  * { box-sizing: border-box; margin: 0; padding: 0; }
  html, body { width: 903px; height: 1200px; overflow: hidden; background: var(--page); }
  .canvas { position: relative; width: 903px; height: 1200px; }

  .card {
    position: absolute; left: 30px; width: 843px; height: 560px;
    overflow: hidden; box-shadow: 0 4px 14px rgba(0,0,0,.25);
  }
  .card--front { top: 24px; }
  .card--back { top: 616px; background: var(--green-pale); }

  /* front */
  .lawn-photo {
    position: absolute; inset: 0;
    background:
      linear-gradient(180deg, #2e4a22 0%, #5d7a40 22%, #d9dcd6 30%, #7aa04a 40%, #4f9a1c 60%, #3d8a14 100%);
  }
  .front-wave { position: absolute; inset: 0; width: 843px; height: 560px; }

  .offer-box {
    position: absolute; left: 533px; width: 232px;
    background: var(--green-deep); color: var(--white);
    border: 3px solid #e8efe4; border-radius: 10px;
    font-family: "Oswald", sans-serif; font-weight: 600; text-align: center;
    line-height: 1.2; padding-top: 6px;
  }
  .offer-box--discount { top: 49px; height: 96px; font-size: 20px; }
  .offer-box--discount .offer-lead { font-size: 27px; line-height: 1.1; }
  .offer-box--featured { top: 152px; height: 100px; font-size: 20px; padding-top: 10px; }

  .estimate-badge { position: absolute; left: 580px; top: 282px; width: 122px; height: 140px; }
  .estimate-badge text { font-family: "Open Sans", sans-serif; }

  .brand {
    position: absolute; font-family: "Oswald", sans-serif; font-weight: 700;
    color: var(--ink); text-transform: uppercase; line-height: 1;
  }
  .brand-name { display: block; letter-spacing: -1px; }
  .brand-tagline { display: block; }
  .card--front .brand { left: 70px; top: 392px; }
  .card--front .brand-name { font-size: 92px; }
  .card--front .brand-tagline { font-size: 28px; margin-top: 4px; letter-spacing: -.5px; }

  .phones { position: absolute; font-family: "Archivo Black", sans-serif; line-height: 1.3; }
  .card--front .phones { left: 480px; top: 446px; font-size: 34px; color: var(--ink); }

  /* back */
  .leaf-texture {
    position: absolute; inset: 0;
    background: radial-gradient(ellipse at 70% 45%, #ffffff 0%, #f4f9e8 40%, #dcedb8 100%);
  }
  .tree-art {
    position: absolute; left: 0; top: 150px; width: 210px; height: 300px;
    border-radius: 0 50% 50% 0;
    background: radial-gradient(ellipse at 35% 45%, #8cc63f 0%, #6bb02c 55%, rgba(107,176,44,0) 75%);
  }
  .grass-art {
    position: absolute; left: 0; bottom: 0; width: 100%; height: 150px;
    background: linear-gradient(180deg, rgba(140,198,63,0) 0%, #a8d65a 35%, #7fbf32 100%);
  }
  .card--back .brand { left: 180px; top: 22px; }
  .card--back .brand-name { font-size: 70px; }
  .card--back .brand-tagline { font-size: 26px; letter-spacing: -.5px; }

  .mail-address {
    position: absolute; left: 470px; top: 52px;
    font-family: "Oswald", sans-serif; font-weight: 600; font-size: 17px;
    color: var(--ink); line-height: 1.3; font-style: normal;
  }
  .services-title {
    position: absolute; left: 200px; top: 142px;
    font-family: "Oswald", sans-serif; font-weight: 700; font-size: 26px;
    color: var(--green-deep); text-transform: uppercase; line-height: 1.2;
  }
  .service-list {
    position: absolute; left: 212px; top: 186px; list-style: none;
    font-family: "Oswald", sans-serif; font-weight: 600; font-size: 19px;
    color: var(--green-deep); line-height: 25px;
  }
  .service-list li { position: relative; padding-left: 20px; }
  .service-list li::before {
    content: ""; position: absolute; left: 0; top: 10px;
    width: 6px; height: 6px; background: var(--green-deep); transform: rotate(45deg);
  }
  .estimate-seal {
    position: absolute; left: 100px; top: 370px; width: 104px; height: 104px;
    border-radius: 50%; background: var(--green); border: 3px solid #e9f3df;
    color: var(--white); text-align: center; font-family: "Open Sans", sans-serif;
    display: flex; flex-direction: column; justify-content: center; line-height: 1.05;
  }
  .estimate-seal .seal-lead { font-weight: 800; font-size: 22px; }
  .estimate-seal .seal-mid { font-weight: 600; font-size: 15px; }
  .estimate-seal .seal-call { font-weight: 800; font-size: 12px; }
  .card--back .phones {
    left: 222px; top: 374px; font-family: "Oswald", sans-serif; font-weight: 700;
    font-size: 32px; color: var(--ink); line-height: 1.15;
  }
  .web-contact {
    position: absolute; left: 112px; top: 460px; list-style: none;
    font-family: "Oswald", sans-serif; font-weight: 600; font-size: 18px;
    color: var(--ink); line-height: 1.4;
  }
  .web-contact li { display: flex; align-items: center; gap: 8px; }
  .web-contact svg { width: 16px; height: 16px; flex: none; }
</style>
</head>
<body>
<main class="canvas">

  <section class="card card--front" aria-label="Postcard front">
    <div class="lawn-photo" role="img" aria-label="Photo of a freshly striped green lawn in front of a white house with flowering shrubs"></div>
    <svg class="front-wave" viewBox="0 0 843 560" aria-hidden="true">
      <defs>
        <linearGradient id="waveGreen" x1="0" y1="0" x2="1" y2="0">
          <stop offset="0" stop-color="#2f9a12"/>
          <stop offset="1" stop-color="#0a6a0a"/>
        </linearGradient>
      </defs>
      <path d="M0,400 C140,330 300,335 450,405 C600,470 720,450 843,360 L843,560 L0,560 Z" fill="#d7dad6"/>
      <path d="M0,418 C140,352 300,360 450,428 C600,492 720,470 843,380 L843,560 L0,560 Z" fill="url(#waveGreen)"/>
    </svg>

    <div class="offer-box offer-box--discount">
      <div class="offer-lead">10% OFF</div>
      <div>first months service</div>
      <div>with signed contract</div>
    </div>
    <div class="offer-box offer-box--featured">
      <div>FEATURED SERVICE</div>
      <div>Weekly Lawn Mowing</div>
      <div>starting at $15/cutting</div>
    </div>

    <svg class="estimate-badge" viewBox="0 0 122 140" aria-label="Contact us now for a free estimate">
      <path d="M8,6 Q8,0 14,0 H108 Q114,0 114,6 V88 L61,138 L8,88 Z" fill="#3a4048" stroke="#9aa0a6" stroke-width="2"/>
      <text x="61" y="22" text-anchor="middle" font-size="11" fill="#ffffff">CONTACT US NOW</text>
      <rect x="0" y="32" width="122" height="42" fill="#4fae1e"/>
      <text x="61" y="49" text-anchor="middle" font-size="13" font-weight="800" fill="#ffffff">FREE</text>
      <text x="61" y="67" text-anchor="middle" font-size="13" font-weight="800" fill="#ffffff">ESTIMATE</text>
      <path d="M22,92 L61,122 L100,92 L100,104 L61,134 L22,104 Z" fill="#4fae1e"/>
    </svg>

    <div class="brand">
      <span class="brand-name">Velmora</span>
      <span class="brand-tagline">Property Management</span>
    </div>
    <div class="phones">
      <div>800-555-0142</div>
      <div>908-555-0187</div>
    </div>
  </section>

  <section class="card card--back" aria-label="Postcard back">
    <div class="leaf-texture" role="img" aria-label="Soft pale green leaf pattern background"></div>
    <div class="tree-art" role="img" aria-label="Illustration of a leafy green tree"></div>
    <div class="grass-art" role="img" aria-label="Illustration of green grass along the bottom edge"></div>

    <div class="brand">
      <span class="brand-name">Velmora</span>
      <span class="brand-tagline">Property Management</span>
    </div>
    <address class="mail-address">
      PO Box 418<br>Ferncliff, NJ 08790
    </address>

    <h2 class="services-title">Residential Services</h2>
    <ul class="service-list">
      <li>Weekly lawn mowing &amp; care</li>
      <li>Landscape service</li>
      <li>Spring and fall clean up</li>
      <li>Lawn and flower bed care</li>
      <li>Pest and weed control</li>
      <li>Fertilizing</li>
      <li>Planting and more</li>
    </ul>

    <div class="estimate-seal">
      <span class="seal-lead">FREE</span>
      <span class="seal-mid">Estimates</span>
      <span class="seal-call">CALL<br>Today</span>
    </div>
    <div class="phones">
      <div>800-555-0142</div>
      <div>908-555-0187</div>
    </div>

    <ul class="web-contact">
      <li>
        <svg viewBox="0 0 16 16" aria-hidden="true"><circle cx="8" cy="8" r="7" fill="none" stroke="#141414" stroke-width="1.5"/><rect x="7.2" y="7" width="1.6" height="5" fill="#141414"/><circle cx="8" cy="4.6" r="1" fill="#141414"/></svg>
        www.velmorapropertymanagement.com
      </li>
      <li>
        <svg viewBox="0 0 16 16" aria-hidden="true"><rect x="1" y="3" width="14" height="10" fill="none" stroke="#141414" stroke-width="1.5"/><path d="M1,3 L8,9 L15,3" fill="none" stroke="#141414" stroke-width="1.5"/></svg>
        velmoraproperty@mailbox.com
      </li>
    </ul>
  </section>

</main>
</body>
</html>
```